Futuristic Trade Show Booth Design for Quorin Builders, Quorin Designers, and Quorin Corporate

We are seeking a cutting-edge and visually striking trade show booth design that showcases the synergy between our three brands: Quorin Designers (architectural design), Quorin Builders (construction services), and Quorin Corporate (unified identity). The design must reflect our commitment to innovation, professionalism, and forward-thinking solutions for commercial design and construction.

The booth will include three panels and two podiums, with a modern and futuristic aesthetic. The focus is on creating a cohesive yet distinctive identity for each brand while highlighting their integration under Quorin Corporate. Here’s what we envision:

Booth Specifications:
Backdrop Dimensions: Three panels of equal size.
Podiums: Two, one representing Quorin Designers and the other Quorin Builders.
Color Palette: Red (#D00E07), dark gray (#3B3838), light gray (#E0E0E0), and white (#FFFFFF).
Panel Breakdown:
1. Left Panel: Quorin Designers (Architectural Focus)

Content:
Taglines like “Design Smarter”
Highlight Quorin Designers’ architectural services : Commercial Architecture, Space Planning, Interior Design, Master Planning, 3D Renderings).
Visuals:
Include high-resolution 3D renderings of commercial spaces and modern blueprints.
Use a gradient background (dark gray to light gray) with overlays of translucent grids.
Icons representing architectural precision (e.g., drafting tools, rulers).
2. Center Panel: Quorin Corporate (Unified Identity)
Content:
Central tagline: “Intergrated Design-Build Solution”
Unified messaging emphasizing Quorin Corporate’s leadership in integrated design-build services.
Showcase how Quorin Designers and Quorin Builders collaborate seamlessly under Quorin Corporate.
Visuals:
A split image showing half blueprints (design) and half construction (build).
Gradient background transitioning from red to gray for continuity.
Icons or a flowchart highlighting the steps: “Concept > Design > Build > Completion.”
3. Right Panel: Quorin Builders (Construction Focus)

Content:
Taglines like “BUILD SMARTER
Highlight Quorin Builders’ construction services (Construction Management, Design-Build, General Contracting, Pre-Construction).
Visuals:

Overlay dynamic construction elements like cranes, scaffolding, and hard hats.
LED accents or subtle motion graphics to emphasize innovation.
Podium Design:
Quorin Designers Podium:
Gray-themed with the Quorin Designers logo and tagline: “DESIGN SMARTER”
Quorin Builders Podium:
Red-themed with the Quorin Builders logo and tagline: “BUILD SMARTER.”
Design Requirements:
Must reflect a modern and futuristic aesthetic.
Use clean, bold typography (e.g., Yantramanav or similar).
Ensure cohesive branding across all panels while keeping individual identities for Quorin Designers, Quorin Builders, and Quorin Corporate.
Balance professionalism with engaging visuals to attract visitors at the trade show.
Additional Notes:
The booth will serve as a centerpiece for showcasing Quorin Corporate’s integrated approach to commercial design and construction. The design must communicate trust, innovation, and expertise while captivating the audience at first glance.

Quorin Builders Website: www.quorinbuilders.example
Quorin Designers Website: www.quorindesigners.example
Quorin Corporate: www.quorincorporate.example
Logo Quorin Builders: https://files.example.net/share/a81kd92jfq0
Logo Quorin Designers: https://files.example.net/share/b27xm41pzr5
Logo Quorin Corporate: https://files.example.net/share/c63vn08twe2
The booth information and spec is on : https://www.standvelt.example/stand-ideas/linkline-10x10-stands/linkline-10x10-exhibit-stand-kit-c/

Target Market(s)

Commercial Property Developers, Corporate Real Estate Managers, Franchise Construction VP, Retail Franchise Owners,

Industry/Entity Type

Commercial Construction, Commercial Architecture

Font styles to use
Other font styles liked:
• Open to others but like Yantramanav, Poppins, Montserrat

Colors
EB3D1F
EC4F4E
F09395
F8D3D4
FCEDEE

Requirements
Must have
• Clear and prominent branding for Quorin Designers, Quorin Builders, and Quorin Corporate on their respective panels. Consistent color scheme using red (#D00E07), dark gray (#3B3838), light gray (#E0E0E0), and white (#FFFFFF) to unify the design. A modern and futuristic aesthetic that reflects innovation, precision, and professionalism. Distinct yet cohesive representation of services offered by Quorin Designers (architectural design), Quorin Builders (construction), and Quorin Corporate (integrated solutions).
Nice to have
• Subtle motion graphics or holographic overlays on panels to enhance the modern feel. A unified gradient background transitioning from red to gray to connect all panels visually. Visual flowcharts showing the step-by-step process of design-build services. Interactive design elements such as QR codes
Should not have
• Overly cluttered design that detracts from key messages or visuals. Fonts that are hard to read or do not match the modern and professional aesthetic. Excessive use of unrelated colors or mismatched visual styles. Misalignment or lack of clear separation between Quorin Designers, Quorin Builders, and Quorin Corporate branding.

```html
<!DOCTYPE html>
<html lang="en">
<head>
<meta charset="utf-8">
<title>Quorin Trade Show Booth – Panels and Podiums</title>
<link rel="stylesheet" href="https://fonts.googleapis.com/css2?family=Oswald:wght@500;700&family=Yantramanav:wght@400;500;700;900&display=swap">
<style>
  :root{
    --red:#d00e07;
    --red-soft:#ec4f4e;
    --dark:#3b3838;
    --ink:#222020;
    --light:#e0e0e0;
    --paper:#ffffff;
    --stage:#d9d9d9;
    --head:"Oswald", sans-serif;
    --body:"Yantramanav", sans-serif;
  }
  *{box-sizing:border-box;margin:0;padding:0}
  html,body{width:835px;height:1200px;overflow:hidden;background:var(--paper);font-family:var(--body);color:var(--dark)}
  .canvas{position:relative;width:835px;height:1200px}

  /* ---------- backdrop panels ---------- */
  .backdrop{position:absolute;left:0;top:0;width:835px;height:528px;background:var(--paper)}
  .panel{position:absolute;top:56px;width:205px;height:434px;background:var(--paper);overflow:hidden;box-shadow:0 2px 6px rgba(0,0,0,.35)}
  .panel--designers{left:66px}
  .panel--corporate{left:315px}
  .panel--builders{left:562px}

  .brand{position:absolute;left:0;right:0;top:0;height:34px;display:flex;align-items:center;gap:6px;padding-left:12px;font-family:var(--body);font-weight:700;font-size:12px;letter-spacing:.5px;text-transform:uppercase;color:var(--dark)}
  .brand__mark{width:12px;height:12px;background:var(--red)}
  .panel--corporate .brand{background:var(--dark);color:var(--paper)}

  .visual{position:absolute;left:0;right:0;top:34px;height:118px}
  .visual--designers{background:linear-gradient(135deg,#6e6a69,#b9b6b4 55%,#e6e2dc)}
  .visual--corporate{background:linear-gradient(135deg,#1f3f7a,#3f6fb0 55%,#9db5d8)}
  .visual--builders{background:linear-gradient(135deg,#f1f1f1,#d8c08a 45%,#f0c419 65%,#9a9a9a)}
  .visual-frame{position:absolute;left:0;top:34px;width:205px;height:150px}

  .headline{position:absolute;left:0;right:0;top:174px;text-align:center;font-family:var(--head);font-weight:700;text-transform:uppercase;line-height:.95}
  .headline__top{display:block;font-size:40px;color:var(--ink)}
  .headline__bottom{display:block;font-size:40px;color:var(--red)}

  .services-title{position:absolute;left:0;right:0;top:258px;text-align:center;font-family:var(--body);font-weight:700;font-size:12px;line-height:1.1;color:var(--red)}
  .services-title small{display:block;font-size:11px;color:var(--dark);font-weight:500}

  .services{position:absolute;left:14px;right:10px;top:288px;display:grid;grid-template-columns:1fr 1fr;gap:5px 6px;list-style:none}
  .services li{display:flex;align-items:center;gap:4px;font-size:7.5px;font-weight:500;line-height:1.05;color:var(--dark)}
  .hex{flex:none;width:16px;height:16px}

  .sketch{position:absolute;left:10px;right:10px;height:44px;background:linear-gradient(180deg,#ffffff,#ececec);opacity:.9}

  .contact{position:absolute;left:0;right:0;top:392px;text-align:center}
  .phone{display:inline-flex;align-items:center;gap:5px;font-family:var(--body);font-weight:900;font-size:19px;color:var(--ink)}
  .phone svg{width:16px;height:16px}
  .web{display:block;font-size:8px;font-weight:500;color:var(--red);margin-top:1px}

  /* centre panel specifics */
  .integrated{position:absolute;top:184px;left:0;right:0;text-align:center;font-family:var(--head);font-weight:700;font-size:20px;color:var(--ink);line-height:1}
  .solution{position:absolute;top:206px;left:10px;right:10px;border:2px solid var(--ink);padding:2px 0 3px;text-align:center;font-family:var(--head);font-weight:700;font-size:18px;line-height:1}
  .solution__top{display:block;color:var(--red)}
  .solution__bottom{display:block;color:var(--ink)}
  .corporate-note{position:absolute;top:254px;left:10px;right:10px;text-align:center;font-size:9px;line-height:1.1;color:var(--ink)}
  .corporate-note strong{display:block;font-size:11px;color:var(--red);font-weight:700;margin-top:1px}
  .services-bar{position:absolute;top:292px;left:26px;right:26px;background:var(--ink);color:var(--paper);text-align:center;font-size:8px;font-weight:700;letter-spacing:.8px;padding:2px 0}
  .flow{position:absolute;top:311px;left:8px;right:8px;display:flex;align-items:center;justify-content:space-between}
  .flow__step{width:38px;height:15px;display:flex;align-items:center;justify-content:center;font-size:6.5px;font-weight:700;color:var(--paper);background:var(--red)}
  .flow__step--gray{background:#8a8787}
  .flow__arrow{width:8px;height:8px}
  .visual--site{position:absolute;left:0;right:0;top:332px;height:68px;background:linear-gradient(135deg,#9b9ea3,#c9ccd1 50%,#7d8187)}
  .contact-bar{position:absolute;left:0;right:0;bottom:0;height:34px;background:var(--ink);display:flex;align-items:center;justify-content:center;gap:6px;font-family:var(--body);font-weight:900;font-size:17px;color:var(--paper)}
  .contact-bar svg{width:15px;height:15px}

  /* ---------- podiums ---------- */
  .stage{position:absolute;left:0;top:528px;width:835px;height:672px;background:var(--stage)}
  .podium{position:absolute;left:78px;width:687px;height:212px;background:linear-gradient(180deg,#ffffff,#ececec);overflow:hidden;box-shadow:0 2px 5px rgba(0,0,0,.25)}
  .podium--designers{top:96px}
  .podium--builders{top:390px}
  .podium svg.band{position:absolute;left:0;top:0;width:687px;height:212px}
  .podium .brand{position:relative;justify-content:center;padding:0;height:auto;top:14px;font-size:13px}
  .podium__tagline{position:absolute;left:0;right:0;top:82px;text-align:center;font-family:var(--head);font-weight:700;font-size:32px;color:var(--paper);letter-spacing:.5px}
  .podium__ghost{position:absolute;top:64px;font-family:var(--head);font-weight:700;font-size:72px;line-height:1;text-transform:uppercase;color:transparent;-webkit-text-stroke:1.5px rgba(255,255,255,.35)}
  .podium__ghost--left{left:14px}
  .podium__ghost--right{right:14px}
  .podium--designers .podium__ghost{-webkit-text-stroke-color:rgba(120,120,120,.45)}
  .podium--builders .podium__ghost{-webkit-text-stroke-color:rgba(180,20,15,.45)}
  .podium__sketch{position:absolute;right:40px;top:30px;width:90px;height:60px;background:linear-gradient(180deg,rgba(255,255,255,0),rgba(200,200,200,.45))}
  .podium__web{position:absolute;left:0;right:0;bottom:18px;text-align:center;font-size:11px;font-weight:700;color:var(--ink)}
</style>
</head>
<body>
<div class="canvas">

  <section class="backdrop">

    <!-- Designers panel -->
    <article class="panel panel--designers">
      <div class="brand"><span class="brand__mark"></span>Quorin Designers</div>
      <div class="visual visual--designers" role="img" aria-label="3D rendering of a modern commercial building"></div>
      <svg class="visual-frame" viewBox="0 0 205 150" aria-hidden="true">
        <polygon points="0,100 60,118 0,150" fill="#3b3838"/>
        <polygon points="0,118 80,140 205,96 205,150 0,150" fill="#ffffff"/>
        <polygon points="120,122 205,92 205,108 138,130" fill="#d00e07"/>
        <polygon points="140,0 205,0 205,60" fill="#3b3838" opacity=".75"/>
      </svg>
      <h2 class="headline"><span class="headline__top">Design</span><span class="headline__bottom">Smarter</span></h2>
      <p class="services-title">Quorin Designers'<small>Architectural Services</small></p>
      <ul class="services">
        <li><svg class="hex" viewBox="0 0 16 16"><polygon points="8,0 15,4 15,12 8,16 1,12 1,4" fill="#3b3838"/></svg>Commercial Architecture</li>
        <li><svg class="hex" viewBox="0 0 16 16"><polygon points="8,0 15,4 15,12 8,16 1,12 1,4" fill="#3b3838"/></svg>Space Planning</li>
        <li><svg class="hex" viewBox="0 0 16 16"><polygon points="8,0 15,4 15,12 8,16 1,12 1,4" fill="#3b3838"/></svg>Interior Design</li>
        <li><svg class="hex" viewBox="0 0 16 16"><polygon points="8,0 15,4 15,12 8,16 1,12 1,4" fill="#3b3838"/></svg>Master Planning</li>
        <li><svg class="hex" viewBox="0 0 16 16"><polygon points="8,0 15,4 15,12 8,16 1,12 1,4" fill="#3b3838"/></svg>3D Renderings</li>
      </ul>
      <div class="sketch" style="top:346px" role="img" aria-label="Faint architectural line sketch of buildings"></div>
      <div class="contact">
        <span class="phone"><svg viewBox="0 0 16 16"><circle cx="8" cy="8" r="8" fill="#d00e07"/><path d="M5.2 4.2l1.5-.4.8 2-1 .7c.5 1.2 1.3 2 2.5 2.5l.7-1 2 .8-.4 1.5c-3.6.2-6.5-2.7-6.1-6.1z" fill="#fff"/></svg>555.014.2290</span>
        <span class="web">www.quorindesigners.example</span>
      </div>
    </article>

    <!-- Corporate panel -->
    <article class="panel panel--corporate">
      <div class="brand"><span class="brand__mark"></span>Quorin Corporate</div>
      <div class="visual visual--corporate" role="img" aria-label="Blueprints with drafting tools and a building rendering"></div>
      <svg class="visual-frame" viewBox="0 0 205 150" aria-hidden="true">
        <polygon points="0,112 205,92 205,118 0,136" fill="#d00e07"/>
        <polygon points="0,136 205,118 205,150 0,150" fill="#ffffff"/>
      </svg>
      <h2 class="integrated">INTERGRATED</h2>
      <p class="solution"><span class="solution__top">DESIGN-BUILD</span><span class="solution__bottom">SOLUTION</span></p>
      <p class="corporate-note">Unified messaging emphasizing<strong>Quorin Corporate's leadership in Integrated</strong></p>
      <p class="services-bar">DESIGN-BUILD SERVICES</p>
      <div class="flow">
        <span class="flow__step">Concept</span>
        <svg class="flow__arrow" viewBox="0 0 8 8"><polygon points="0,0 8,4 0,8" fill="#3b3838"/></svg>
        <span class="flow__step flow__step--gray">Design</span>
        <svg class="flow__arrow" viewBox="0 0 8 8"><polygon points="0,0 8,4 0,8" fill="#3b3838"/></svg>
        <span class="flow__step">Build</span>
        <svg class="flow__arrow" viewBox="0 0 8 8"><polygon points="0,0 8,4 0,8" fill="#3b3838"/></svg>
        <span class="flow__step flow__step--gray">Completion</span>
      </div>
      <div class="visual--site" role="img" aria-label="Blueprint drawing blending into a construction site"></div>
      <div class="contact-bar"><svg viewBox="0 0 16 16"><circle cx="8" cy="8" r="8" fill="#d00e07"/><path d="M5.2 4.2l1.5-.4.8 2-1 .7c.5 1.2 1.3 2 2.5 2.5l.7-1 2 .8-.4 1.5c-3.6.2-6.5-2.7-6.1-6.1z" fill="#fff"/></svg>(555) 014 7833</div>
    </article>

    <!-- Builders panel -->
    <article class="panel panel--builders">
      <div class="brand"><span class="brand__mark"></span>Quorin Builders</div>
      <div class="visual visual--builders" role="img" aria-label="Hard hat, drafting tools and plans on a desk"></div>
      <svg class="visual-frame" viewBox="0 0 205 150" aria-hidden="true">
        <polygon points="0,0 34,0 0,40" fill="#d00e07"/>
        <polygon points="0,96 205,112 205,150 0,150" fill="#d00e07"/>
        <polygon points="0,112 205,128 205,150 0,150" fill="#ffffff"/>
      </svg>
      <h2 class="headline"><span class="headline__top">Build</span><span class="headline__bottom">Smarter</span></h2>
      <p class="services-title">Quorin Builders'<small>Construction Services</small></p>
      <ul class="services">
        <li><svg class="hex" viewBox="0 0 16 16"><polygon points="8,0 15,4 15,12 8,16 1,12 1,4" fill="#3b3838"/></svg>Construction Management</li>
        <li><svg class="hex" viewBox="0 0 16 16"><polygon points="8,0 15,4 15,12 8,16 1,12 1,4" fill="#3b3838"/></svg>General Contracting</li>
        <li><svg class="hex" viewBox="0 0 16 16"><polygon points="8,0 15,4 15,12 8,16 1,12 1,4" fill="#3b3838"/></svg>Design-Build</li>
        <li><svg class="hex" viewBox="0 0 16 16"><polygon points="8,0 15,4 15,12 8,16 1,12 1,4" fill="#3b3838"/></svg>Pre-Construction</li>
      </ul>
      <div class="sketch" style="top:336px" role="img" aria-label="Faint line sketch of a building under construction"></div>
      <div class="contact">
        <span class="phone"><svg viewBox="0 0 16 16"><circle cx="8" cy="8" r="8" fill="#d00e07"/><path d="M5.2 4.2l1.5-.4.8 2-1 .7c.5 1.2 1.3 2 2.5 2.5l.7-1 2 .8-.4 1.5c-3.6.2-6.5-2.7-6.1-6.1z" fill="#fff"/></svg>555.014.2290</span>
        <span class="web">www.quorinbuilders.example</span>
      </div>
    </article>
  </section>

  <section class="stage">

    <article class="podium podium--designers">
      <div class="podium__sketch" role="img" aria-label="Faint line sketch of tall buildings"></div>
      <svg class="band" viewBox="0 0 687 212" aria-hidden="true">
        <polygon points="0,60 150,60 205,86 480,86 535,52 687,52 687,130 535,130 480,156 205,156 150,124 0,124" fill="#3b3838"/>
      </svg>
      <span class="podium__ghost podium__ghost--left">Design</span>
      <span class="podium__ghost podium__ghost--right">Smarter</span>
      <div class="brand"><span class="brand__mark"></span>Quorin Designers</div>
      <h3 class="podium__tagline">DESIGN SMARTER</h3>
      <p class="podium__web">www.quorindesigners.example</p>
    </article>

    <article class="podium podium--builders">
      <svg class="band" viewBox="0 0 687 212" aria-hidden="true">
        <polygon points="0,60 150,60 205,86 480,86 535,52 687,52 687,130 535,130 480,156 205,156 150,124 0,124" fill="#d00e07"/>
      </svg>
      <span class="podium__ghost podium__ghost--left">Build</span>
      <span class="podium__ghost podium__ghost--right">Smarter</span>
      <div class="brand"><span class="brand__mark"></span>Quorin Builders</div>
      <h3 class="podium__tagline">BUILD SMARTER</h3>
      <p class="podium__web">www.quorinbuilders.example</p>
    </article>
  </section>

</div>
</body>
</html>
```